Catholic composer needs poster for new musical, "THE STONE AND THE VIGIL, the Harvest Musical"

We need a dynamic poster for "The Stone and the Vigil," a new musical written for Catholic dinner theater. We need you to create an iconic design like you see in posters for classic musicals, like "Rosa Calendula," Lantern of the Harbour," or "Gilded." In our musical, “fire” represents the Holy Spirit, who showers man with his merciful love.

Miraculous events occur. A mighty wind from heaven fills the house. Tongues of fire appear over their heads. They speak in other tongues that are understandable by all present. They are emboldened to go out and tell the Good News to the world, despite the risks associated with evangelizing this fledgling religion. They exclaim, “Lord, you will show us the path to life.”

Target Market(s)

The audience is adult members of Catholic churches. But don't make the design look too "churchy."

Requirements
Must have
• Photoshop or Illustrated file with layers, or vector format.
Should not have
• Really don't want photos.

```html
<!DOCTYPE html>
<html lang="en">
<head>
<meta charset="utf-8">
<title>The Stone and the Vigil – Poster</title>
<link rel="stylesheet" href="https://fonts.googleapis.com/css2?family=Cinzel:wght@700;900&family=Montserrat:wght@400;600&family=Playfair+Display:ital,wght@1,400&display=swap">
<style>
  :root {
    --bg-deep: #0d0c0e;
    --bg-mid: #1d1a1c;
    --ember: #e9782a;
    --ember-soft: rgba(233, 120, 42, 0.55);
    --sky-glow: rgba(60, 140, 220, 0.45);
    --silver-light: #f3efe8;
    --silver-mid: #b9b2a8;
    --steel-light: #dfefff;
    --steel-mid: #6fa6d8;
    --steel-dark: #27527f;
    --text-soft: #d9d4cc;
    --text-dim: #8d8780;
    --rule: rgba(220, 214, 205, 0.45);
  }
  * { margin: 0; padding: 0; box-sizing: border-box; }
  html, body {
    width: 874px; height: 1200px; overflow: hidden;
    background: var(--bg-deep);
  }
  .poster {
    position: relative;
    width: 874px; height: 1200px;
    overflow: hidden;
    background:
      radial-gradient(ellipse 70% 40% at 50% 32%, rgba(120, 60, 30, 0.35), transparent 70%),
      linear-gradient(180deg, var(--bg-mid) 0%, var(--bg-deep) 100%);
    color: var(--text-soft);
    text-align: center;
  }
  .ember-field {
    position: absolute; inset: 0;
    background:
      radial-gradient(circle 140px at 22% 34%, var(--ember-soft), transparent 70%),
      radial-gradient(circle 90px at 80% 22%, rgba(233, 120, 42, 0.35), transparent 70%),
      radial-gradient(circle 160px at 78% 58%, var(--sky-glow), transparent 70%),
      radial-gradient(circle 110px at 15% 62%, rgba(60, 140, 220, 0.25), transparent 70%);
  }
  .flare {
    position: absolute; left: 0; right: 0; top: 455px; height: 40px;
    background: radial-gradient(ellipse 50% 50% at 50% 50%, rgba(255, 230, 200, 0.9), rgba(120, 180, 255, 0.35) 35%, transparent 70%);
  }
  .flare-core {
    position: absolute; left: 50%; top: 462px; width: 70px; height: 26px;
    transform: translateX(-50%);
    background: radial-gradient(ellipse at center, #fffaf0 0%, rgba(255, 200, 140, 0.8) 35%, transparent 70%);
  }
  .eyebrow {
    position: absolute; top: 62px; left: 0; right: 0;
    font-family: "Montserrat", sans-serif; font-weight: 400;
    font-size: 20px; letter-spacing: 9px; color: var(--text-dim);
  }
  .title { position: absolute; left: 0; right: 0; top: 170px; }
  .title-line {
    display: block;
    font-family: "Cinzel", serif; font-weight: 900;
    line-height: 1;
    -webkit-background-clip: text; background-clip: text;
    color: transparent;
  }
  .title-first {
    font-size: 104px; letter-spacing: 2px;
    background-image: linear-gradient(180deg, var(--silver-light) 0%, var(--silver-mid) 45%, #7b5a3e 60%, var(--silver-light) 100%);
    text-shadow: 0 0 30px rgba(233, 120, 42, 0.25);
  }
  .title-amp {
    font-size: 44px; margin: 30px 0 20px;
    background-image: linear-gradient(180deg, #fff4e4, #e8b889);
  }
  .title-second {
    font-size: 168px; letter-spacing: 6px;
    background-image: linear-gradient(180deg, var(--steel-light) 0%, var(--steel-mid) 45%, var(--steel-dark) 62%, var(--steel-light) 100%);
  }
  .tagline {
    position: absolute; top: 790px; left: 0; right: 0;
    font-family: "Playfair Display", serif; font-style: italic;
    font-size: 50px; line-height: 1.15; color: var(--silver-light);
  }
  .credit {
    position: absolute; top: 955px; left: 200px; right: 200px;
    border-top: 1px solid var(--rule);
    border-bottom: 1px solid var(--rule);
    padding: 16px 0;
    font-family: "Montserrat", sans-serif; font-weight: 400;
    font-size: 18px; letter-spacing: 3px; line-height: 1.6;
    color: var(--text-soft);
  }
  .credit-name { font-weight: 600; color: var(--silver-light); }
</style>
</head>
<body>
  <main class="poster">
    <div class="ember-field" role="img" aria-label="Drifting sparks and embers in warm orange and cool blue light"></div>
    <div class="flare"></div>
    <div class="flare-core"></div>

    <p class="eyebrow">THE HARVEST MUSICAL</p>

    <h1 class="title">
      <span class="title-line title-first">THE STONE</span>
      <span class="title-line title-amp">&amp;</span>
      <span class="title-line title-second">VIGIL</span>
    </h1>

    <p class="tagline">“O Spirit come,<br>You are merciful love”</p>

    <p class="credit">A NEW MUSICAL FOR CATHOLIC DINNER THEATER<br>BY <span class="credit-name">PAUL VERRANT</span></p>
  </main>
</body>
</html>
```